Refresh our Logo and Letterhead!

We would like to see designs with blue, green, teal etc. Our current logo and contact details for the letterhead is attached.
We're a small boutique firm based in Sydney, Australia. We're near the coast and not opposed to coastal images. We practice in property law and have primarily female practitioners, although we don't necessarily need the logo and letterhead to be too feminine. We would like to see designs with blue, green, teal etc. Our current logo and contact details for the letterhead is attached.
We're a small boutique firm based in Sydney, Australia. We're near the coast and not opposed to coastal images. We practice in property law and have primarily female practitioners, although we don't necessarily need the logo and letterhead to be too feminine.

Target Market(s)

Young professionals

Industry/Entity Type

Law Firm

Logo Text

Halvering Legal

Font styles to use
Serif
Sans Serif

Colors
34a7d8
00a990
85acd3
886aae

Requirements
Must have
• The letterhead must have the text in the "contact info" jpg uploaded with the brief.
Nice to have
• We'd like to see some simple, innovating, fresh ideas. A watermark or something interesting in the background would be good.

```html
<!DOCTYPE html>
<html lang="en">
<head>
<meta charset="utf-8">
<title>Halvering Legal – Letterhead</title>
<link href="https://fonts.googleapis.com/css2?family=Lato:wght@400;700&family=Roboto+Condensed:wght@300;400&display=swap" rel="stylesheet">
<style>
  :root {
    --brand-dark: #1f62ae;
    --brand-light: #63c3ec;
    --ink: #4f4f4f;
    --ink-soft: #666666;
    --paper: #ffffff;
  }
  * { box-sizing: border-box; margin: 0; padding: 0; }
  html, body { width: 1056px; height: 1200px; overflow: hidden; background: var(--paper); }
  .letterhead {
    position: relative;
    width: 1056px;
    height: 1200px;
    background: var(--paper);
    overflow: hidden;
    font-family: "Roboto Condensed", "Arial Narrow", sans-serif;
    color: var(--ink);
  }
  .brand {
    position: absolute;
    left: 105px;
    top: 138px;
    width: 302px;
    text-align: center;
    font-family: "Lato", sans-serif;
  }
  .brand-name {
    font-weight: 700;
    font-size: 38px;
    line-height: 1;
    color: var(--brand-dark);
    white-space: nowrap;
  }
  .contact {
    position: absolute;
    left: 731px;
    top: 66px;
    font-family: "Lato", sans-serif;
    font-style: normal;
    font-size: 20px;
    color: var(--ink-soft);
    line-height: 21px;
  }
  .contact-address { margin-bottom: 8px; }
  .contact-line { display: flex; align-items: center; gap: 14px; }
  .contact-line svg { width: 16px; height: 16px; fill: var(--brand-dark); flex: none; }
  .letter-body {
    position: absolute;
    left: 99px;
    top: 356px;
    width: 865px;
    font-weight: 300;
    font-size: 23.6px;
    line-height: 30px;
  }
  .salutation { margin-bottom: 24px; }
  .letter-body p.para { text-align: justify; margin-bottom: 28px; }
  .closing {
    position: absolute;
    left: 99px;
    top: 966px;
    font-weight: 300;
    font-size: 23.6px;
  }
  .signature {
    position: absolute;
    left: 95px;
    top: 1006px;
    width: 86px;
    height: 42px;
    background: linear-gradient(90deg, #dbe6f4, #eef3fa);
    border-radius: 4px;
  }
  .footer-band { position: absolute; left: 0; bottom: 0; width: 1056px; height: 40px; }
  .footer-url {
    position: absolute;
    right: 18px;
    bottom: 9px;
    font-family: "Lato", sans-serif;
    font-size: 17px;
    color: #ffffff;
  }
</style>
</head>
<body>
<main class="letterhead">
  <header class="brand">
    <div class="brand-name">Halvering Legal</div>
  </header>

  <address class="contact">
    <div class="contact-address">18 Marlowe Bay Road<br>Seacliff NSW 2263</div>
    <div class="contact-line">
      <svg viewBox="0 0 16 16"><path d="M1 6c0-2 3-3 7-3s7 1 7 3v1h-4V5.5H5V7H1z M3 8h10l1 6H2z"/></svg>
      <span>02 4581 2736</span>
    </div>
    <div class="contact-line">
      <svg viewBox="0 0 16 16"><path d="M4 1h8v14H4z M5.5 2.5v9h5v-9z"/></svg>
      <span>0431 608 259</span>
    </div>
    <div class="contact-line">
      <svg viewBox="0 0 16 16"><path d="M4 1h8v4H4z M1 6h14v6h-3v3H4v-3H1z M5.5 10v3.5h5V10z"/></svg>
      <span>02 8314 9062</span>
    </div>
    <div class="contact-line">
      <svg viewBox="0 0 16 16"><path d="M1 3h14v10H1z" fill="var(--brand-dark)"/><path d="M1.5 3.5 8 9l6.5-5.5" fill="none" stroke="#fff" stroke-width="1.2"/></svg>
      <span>mara@halveringlegal.com.au</span>
    </div>
  </address>

  <section class="letter-body">
    <p class="salutation">Dear Sir/Mam,</p>
    <p class="para">Contrary to popular belief, Lorem Ipsum is not simply random text. It has roots in a piece of classical Latin literature from 45 BC, making it over 2000 years old. Edwin Marsh, a Latin professor at Ashgrove College in Virginia, looked up one of the more obscure Latin words, consectetur.</p>
    <p class="para">Lorem Ipsum comes from sections 1.10.32 and 1.10.33 of "de Finibus Bonorum et Malorum" (The Extremes of Good and Evil) by Aurelius, written in 45 BC. This book is a treatise on the theory of ethics, very popular during the Renaissance. The first line of Lorem Ipsum.</p>
    <p class="para">The standard chunk of Lorem Ipsum used since the 1500s is reproduced below for those interested. Sections 1.10.32 and 1.10.33 from "de Finibus Bonorum et Malorum" by Aurelius are also reproduced in their exact original.</p>
    <p class="para">The standard chunk of Lorem Ipsum used since the 1500s is reproduced below for those interested.</p>
  </section>

  <p class="closing">Best Regards</p>
  <div class="signature" role="img" aria-label="Handwritten signature of the sender"></div>

  <footer>
    <svg class="footer-band" viewBox="0 0 1056 40" preserveAspectRatio="none" aria-hidden="true">
      <polygon points="0,10 266,10 260,17 0,17" fill="var(--brand-light)"/>
      <polygon points="272,10 546,10 540,17 266,17" fill="var(--brand-dark)"/>
      <polygon points="552,10 822,10 816,17 546,17" fill="var(--brand-light)"/>
      <rect x="0" y="28" width="1056" height="12" fill="var(--brand-dark)"/>
      <polygon points="833,4 1056,4 1056,40 805,40" fill="var(--brand-dark)"/>
    </svg>
    <span class="footer-url">www.halveringlegal.com.au</span>
  </footer>
</main>
</body>
</html>
```